Company Business cards ZOV. Modern professional look

We need a new business card design using the new logo you created for us. Make it modern and professional. It has to be simple yet innovative. We are a recruitment and IT Services provider and we are publicly listed so the card has to be of the highest standard and interesting to look at.

Make sure the card is simple but crisp.

Target Market(s)

Clients

Industry/Entity Type

Recruitment

Contact Information for Business Card

Name
Position Title
Company Name
Address
Phone email fax website

Font styles to use
Other font styles liked:
• Calibri

Requirements
Must have
• Modern and professional
Nice to have
• Clean, simple yet interesting
Should not have
• Old style, boring

```html
<!DOCTYPE html>
<html lang="en">
<head>
<meta charset="utf-8">
<title>ZOV Group – Business Card</title>
<link href="https://fonts.googleapis.com/css2?family=Lato:wght@400;700&display=swap" rel="stylesheet">
<style>
  :root {
    --page: #e9eeee;
    --card: #ffffff;
    --panel: #e4e4e4;
    --ink: #1d1d1d;
    --accent: #e3141b;
    --muted: #555555;
  }
  * { box-sizing: border-box; margin: 0; padding: 0; }
  html, body {
    width: 1200px; height: 900px; overflow: hidden;
    background: var(--page);
    font-family: "Lato", "Carlito", sans-serif;
    color: var(--ink);
  }
  .sheet {
    width: 1200px; height: 900px;
    display: flex; flex-direction: column;
    align-items: center; justify-content: center;
    gap: 56px;
  }
  .card {
    position: relative;
    width: 600px; height: 343px;
    background: var(--card);
    box-shadow: 0 2px 4px rgba(0,0,0,.08), 0 10px 24px rgba(0,0,0,.08);
    overflow: hidden;
  }
  /* Front */
  .card-front .panel {
    position: absolute; inset: 0;
    width: 100%; height: 100%;
  }
  .brand {
    position: absolute;
    top: 48px; right: 36px;
    display: flex; align-items: center; gap: 10px;
  }
  .brand-dot {
    width: 14px; height: 14px; border-radius: 50%;
    background: var(--accent);
  }
  .brand-name {
    font-weight: 700; font-size: 40px; letter-spacing: 1px;
    color: var(--ink);
  }
  /* Back */
  .card-back .identity {
    position: absolute; left: 54px; top: 62px;
  }
  .person-name {
    font-size: 30px; font-weight: 400; letter-spacing: .3px;
  }
  .person-title {
    font-size: 16px; color: var(--muted); margin-top: 2px;
  }
  .contact-list {
    position: absolute; left: 54px; top: 162px;
    list-style: none;
    font-size: 16px; line-height: 25px;
  }
  .contact-list li { display: flex; }
  .contact-label {
    width: 22px; color: var(--accent); font-weight: 700;
  }
  .contact-sep { width: 14px; }
  .address {
    position: absolute; left: 54px; top: 270px;
    font-size: 16px; line-height: 23px;
    font-style: normal;
  }
</style>
</head>
<body>
<main class="sheet">

  <section class="card card-front" aria-label="Business card front">
    <svg class="panel" viewBox="0 0 600 343" preserveAspectRatio="none" aria-hidden="true">
      <path d="M0 0 H600 V140 C470 95 300 110 190 160 C110 196 50 250 0 300 Z" fill="var(--panel)"/>
    </svg>
    <div class="brand">
      <span class="brand-dot"></span>
      <span class="brand-name">ZOV Group</span>
    </div>
  </section>

  <section class="card card-back" aria-label="Business card back">
    <div class="identity">
      <h1 class="person-name">Marek Dalvin</h1>
      <p class="person-title">President</p>
    </div>
    <ul class="contact-list">
      <li><span class="contact-label">E</span><span class="contact-sep">:</span><span>info@zovgroup.com</span></li>
      <li><span class="contact-label">T</span><span class="contact-sep">:</span><span>310 555 0142</span></li>
      <li><span class="contact-label">F</span><span class="contact-sep">:</span><span>310 555 0142</span></li>
      <li><span class="contact-label">W</span><span class="contact-sep">:</span><span>zovgroup.com</span></li>
    </ul>
    <address class="address">
      48 Harbor Lane, Westfield<br>Region 40215
    </address>
  </section>

</main>
</body>
</html>
```